Brightwater Valley Strong Unions and Households Initiative-Postcard

We need a postcard to promote our program. We will use the postcard to remind clients of appointments or even use it as a marketing tool when we go out to events. We provide healthy relationship education, financial classes and job readiness education. Our target population is adult couples. Mostly Spanish speaking. If its possible to incorporate all three components into the design that would be great, if not, healthy relationship would be our priority.

Attached is a logo we would like to use.

I have also included the text we would like to use. Would you please make all text editable incase we want to add different text.

The funding statement has to go at the bottom (it can be in small text).

Industry/Entity Type

Marketing

Requirements
Must have
• if you use images of people, please use Latino images. Our target population is Spanish speaking.

```html
<!DOCTYPE html>
<html lang="es">
<head>
<meta charset="utf-8">
<title>Brightwater Valley Strong Unions and Households Initiative – Postcard</title>
<link rel="stylesheet" href="https://fonts.googleapis.com/css2?family=Roboto+Condensed:wght@700&family=Open+Sans:ital,wght@0,400;0,600;1,600&display=swap">
<style>
  :root {
    --stage: #2f2520;
    --paper: #f7f6f4;
    --crimson: #c8184f;
    --royal: #1d4d9c;
    --royal-deep: #0f3a84;
    --navy-text: #1a4f8c;
    --orange: #e98a1f;
    --grey-text: #555a60;
    --mail-grey: #e6e7e9;
    --photo-warm-a: #d9c2ad;
    --photo-warm-b: #8fa6c7;
  }
  * { box-sizing: border-box; margin: 0; padding: 0; }
  html, body { width: 863px; height: 1200px; overflow: hidden; }
  body { background: var(--stage); position: relative; font-family: "Open Sans", sans-serif; }

  .card {
    position: absolute; left: 87px; width: 682px; height: 531px;
    background: var(--paper); overflow: hidden;
  }
  .card--front { top: 53px; }
  .card--back { top: 610px; height: 529px; }
  .card svg.shapes { position: absolute; inset: 0; }

  /* front */
  .services-badge {
    position: absolute; left: 505px; top: 34px; width: 154px; height: 154px;
    border-radius: 50%; background: #fafafa; border: 7px solid var(--crimson);
    display: flex; flex-direction: column; align-items: center; justify-content: center;
    box-shadow: 0 3px 8px rgba(0,0,0,.25);
    font-size: 13px; line-height: 1.35; color: #333; text-align: center;
  }
  .services-badge .item { padding: 2px 6px; }
  .services-badge .item + .item { border-top: 1px solid var(--orange); }

  .program-name {
    position: absolute; right: 33px; top: 240px;
    font-size: 16px; font-weight: 400; color: var(--orange);
  }
  .program-tagline {
    position: absolute; right: 33px; top: 263px; width: 230px; text-align: right;
    font-size: 6.5px; line-height: 1.4; color: var(--navy-text); text-transform: uppercase; font-weight: 600;
  }
  .headline {
    font-family: "Roboto Condensed", sans-serif; font-weight: 700;
    font-size: 33px; line-height: 1.15; letter-spacing: .3px;
  }
  .card--front .headline { position: absolute; right: 33px; top: 296px; text-align: right; color: var(--crimson); }
  .info-call {
    position: absolute; right: 40px; top: 399px;
    font-style: italic; font-weight: 600; font-size: 17px; color: var(--navy-text);
  }
  .phone {
    position: absolute; right: 33px; top: 419px;
    font-family: "Roboto Condensed", sans-serif; font-weight: 700; font-size: 38px; color: var(--royal-deep);
  }
  .funding {
    position: absolute; left: 247px; width: 402px; top: 479px;
    font-size: 9.4px; line-height: 1.42; color: var(--grey-text); text-align: justify;
  }
  .partner-badge {
    position: absolute; left: 43px; top: 325px; width: 194px; height: 194px; border-radius: 50%;
    background: radial-gradient(circle at 45% 40%, #ffffff 60%, #e4e4e4 100%);
    box-shadow: 0 3px 10px rgba(0,0,0,.3);
    display: flex; align-items: center; justify-content: center; text-align: center;
  }
  .partner-name {
    font-weight: 600; font-size: 17px; line-height: 1.2; color: var(--royal); width: 140px;
  }

  /* back */
  .card--back .headline { position: absolute; left: 29px; top: 28px; color: #fff; }
  .mail-zone { position: absolute; background: var(--mail-grey); display: flex; justify-content: center; font-size: 19px; color: #111; font-family: Arial, sans-serif; }
  .mail-zone--postage { left: 512px; top: 16px; width: 153px; height: 152px; align-items: flex-start; padding-top: 68px; text-align: center; line-height: 1.25; }
  .mail-zone--address { left: 330px; top: 168px; width: 335px; height: 265px; align-items: flex-start; padding-top: 40px; }
  .mail-zone--barcode { left: 86px; top: 433px; width: 579px; height: 76px; align-items: center; }
</style>
</head>
<body>

<section class="card card--front" aria-label="Postcard front">
  <svg class="shapes" viewBox="0 0 682 531" width="682" height="531">
    <defs>
      <linearGradient id="groupPhoto" x1="0" y1="0" x2="1" y2="1">
        <stop offset="0" stop-color="var(--photo-warm-a)"/>
        <stop offset="1" stop-color="var(--photo-warm-b)"/>
      </linearGradient>
      <linearGradient id="frontBlue" x1="0" y1="0" x2="1" y2="1">
        <stop offset="0" stop-color="#2d66b8"/>
        <stop offset="1" stop-color="var(--royal-deep)"/>
      </linearGradient>
    </defs>
    <path d="M682 0 V170 C640 110 610 40 480 0 Z" fill="url(#frontBlue)"/>
    <path role="img" aria-label="Photo of a smiling group of young Latino adults giving thumbs up"
          d="M0 0 H520 C500 90 470 170 380 220 C300 262 220 290 150 320 C90 345 40 380 0 420 Z"
          fill="url(#groupPhoto)"/>
    <path d="M520 0 C500 90 470 170 380 220 C300 262 220 290 150 320" fill="none" stroke="#6b2a2a" stroke-width="1.2"/>
    <path d="M535 0 C515 100 480 180 390 232 C320 270 250 295 190 318" fill="none" stroke="var(--crimson)" stroke-width="1"/>
    <path d="M560 0 C610 40 660 100 682 150" fill="none" stroke="var(--royal)" stroke-width="1"/>
    <path d="M40 530 C20 470 60 400 130 385" fill="none" stroke="var(--crimson)" stroke-width="1.5"/>
  </svg>

  <div class="services-badge">
    <div class="item">Healthy<br>Relationship<br>Education</div>
    <div class="item">Financial Classes</div>
    <div class="item">Job Readiness<br>Education</div>
  </div>

  <div class="program-name">Uniones y Hogares Fuertes</div>
  <div class="program-tagline">Fortalecimiento de relaciones | Capacitación financiera<br>y preparación laboral</div>

  <h1 class="headline">…porque una relación<br>sana estáasu alcance</h1>
  <p class="info-call">Para más información, llame a</p>
  <p class="phone">555-014-3556</p>
  <p class="funding">“Funding for this project was provided by the Regional Office of Family Services, Division for Children and Households, Grant: #42BV0917. These services are available to all eligible persons, regardless of race, gender, age, disability, or religion.”</p>

  <div class="partner-badge"><span class="partner-name">Brightwater Valley Community Partners</span></div>
</section>

<section class="card card--back" aria-label="Postcard back">
  <svg class="shapes" viewBox="0 0 682 529" width="682" height="529">
    <defs>
      <radialGradient id="backBlue" cx=".35" cy=".3" r=".8">
        <stop offset="0" stop-color="#3a7bd0"/>
        <stop offset="1" stop-color="var(--royal-deep)"/>
      </radialGradient>
    </defs>
    <path d="M0 0 H400 C420 0 430 60 410 110 C390 150 330 150 290 160 C230 180 200 240 180 300 C160 340 100 330 0 330 Z" fill="url(#backBlue)"/>
    <path d="M400 0 C432 20 432 90 410 120 C390 150 330 155 290 168" fill="none" stroke="var(--royal)" stroke-width="1"/>
    <path d="M408 0 C440 25 438 95 415 128" fill="none" stroke="var(--royal)" stroke-width="1"/>
    <rect role="img" aria-label="Photo of a smiling young Latino couple standing back to back" x="33" y="126" width="272" height="403" fill="#c9c6c4"/>
  </svg>

  <h2 class="headline">…porque una relación<br>sana estáasu alcance</h2>

  <div class="mail-zone mail-zone--postage">Postage<br>Area</div>
  <div class="mail-zone mail-zone--address">Address Area</div>
  <div class="mail-zone mail-zone--barcode">Barcode Area</div>
</section>

</body>
</html>
```